Gablestone Inspections Business Card

I need a business card for my new company. The company is going to provide home inspections. The name of the company is Gablestone Inspections. I am not sure if I want a single sided card or a double. I have a logo already that I want to incorporate into the card design. I was wondering if I should incorporate a catch phrase on my card or not. If I did the phrase would be "The Intelligent Choice for Home Inspections" but i am unsure how or if to use it on a card. The following information needs to be on the card.
Home Inspection
My Name: Tobias R. Fenwick Phone Number: 555-317-6420 Email: tfenwick@gablestoneinspections.com Website: www.gablestoneinspections.com NY HI License # 27300592415

```html
<!DOCTYPE html>
<html lang="en">
<head>
<meta charset="utf-8">
<title>Gablestone Inspections – Business Card</title>
<link href="https://fonts.googleapis.com/css2?family=Open+Sans:wght@400;600;700;800&display=swap" rel="stylesheet">
<style>
  :root {
    --bg: #d9dbde;
    --white: #ffffff;
    --ink: #5d6166;
    --blue: #2a8fd0;
    --blue-deep: #1b6fae;
    --blue-light: #8ccbf0;
    --black: #141414;
    --black-soft: #222325;
  }
  * { box-sizing: border-box; margin: 0; padding: 0; }
  html, body { width: 1200px; height: 929px; overflow: hidden; }
  body { background: var(--bg); font-family: "Open Sans", sans-serif; position: relative; }

  .card {
    position: absolute; width: 560px; height: 320px; overflow: hidden;
    box-shadow: 0 10px 28px rgba(0,0,0,.22);
  }

  /* Front */
  .card-front { left: 60px; top: 90px; background: var(--white); }
  .front-top-band {
    position: absolute; left: 270px; right: 0; top: 52px; height: 32px; background: var(--blue-light);
  }
  .name-tag {
    position: absolute; left: 270px; top: 52px; height: 32px; padding: 0 18px;
    display: flex; align-items: center;
    color: var(--blue-deep); font-weight: 700; font-size: 17px; letter-spacing: .5px; text-transform: uppercase;
  }
  .contact-list { position: absolute; left: 290px; top: 100px; list-style: none; }
  .contact-list li {
    display: flex; align-items: center; gap: 8px; color: var(--ink); font-size: 12.5px; line-height: 21px;
    white-space: nowrap;
  }
  .contact-list svg { width: 12px; height: 12px; fill: var(--blue-deep); flex: none; }
  .front-brand {
    position: absolute; left: 26px; top: 196px; display: flex; align-items: center; gap: 9px;
  }
  .brand-mark { width: 13px; height: 13px; background: var(--blue); flex: none; }
  .brand-name { font-weight: 800; font-size: 21px; color: var(--blue-deep); letter-spacing: .2px; white-space: nowrap; }
  .front-bottom-band {
    position: absolute; left: 0; right: 0; bottom: 0; height: 56px; background: var(--blue);
    display: flex; align-items: center; justify-content: center;
  }
  .license { color: var(--white); font-size: 12.5px; }

  /* Back */
  .card-back {
    left: 580px; top: 510px;
    background: linear-gradient(135deg, var(--black) 0%, var(--black-soft) 55%, var(--black) 100%);
  }
  .back-brand {
    position: absolute; left: 60px; top: 140px; display: flex; align-items: center; gap: 12px;
  }
  .back-brand .brand-mark { width: 16px; height: 16px; background: var(--blue-light); }
  .back-brand .brand-name { color: var(--white); font-size: 29px; }
</style>
</head>
<body>
  <section class="card card-front" aria-label="Business card front">
    <div class="front-top-band"></div>
    <div class="name-tag">Tobias R. Fenwick</div>
    <ul class="contact-list">
      <li><svg viewBox="0 0 24 24"><path d="M6.6 10.8a15 15 0 0 0 6.6 6.6l2.2-2.2a1 1 0 0 1 1-.25 11.4 11.4 0 0 0 3.6.57 1 1 0 0 1 1 1V20a1 1 0 0 1-1 1A17 17 0 0 1 3 4a1 1 0 0 1 1-1h3.5a1 1 0 0 1 1 1c0 1.25.2 2.45.57 3.57a1 1 0 0 1-.25 1z"/></svg>555-317-6420</li>
      <li><svg viewBox="0 0 24 24"><path d="M2 5h20v14H2z M4 7v.5l8 5 8-5V7z" fill-rule="evenodd"/></svg>tfenwick@gablestoneinspections.com</li>
      <li><svg viewBox="0 0 24 24"><path d="M12 2a10 10 0 1 0 0 20 10 10 0 0 0 0-20zm6.9 9h-3a15 15 0 0 0-1.3-5.6A8 8 0 0 1 18.9 11zM12 4c.9 1.2 1.8 3.7 1.9 7h-3.8c.1-3.3 1-5.8 1.9-7zM9.4 5.4A15 15 0 0 0 8.1 11h-3a8 8 0 0 1 4.3-5.6zM5.1 13h3a15 15 0 0 0 1.3 5.6A8 8 0 0 1 5.1 13zM12 20c-.9-1.2-1.8-3.7-1.9-7h3.8c-.1 3.3-1 5.8-1.9 7zm2.6-1.4a15 15 0 0 0 1.3-5.6h3a8 8 0 0 1-4.3 5.6z"/></svg>www.gablestoneinspections.com</li>
    </ul>
    <div class="front-brand">
      <span class="brand-mark"></span>
      <span class="brand-name">Gablestone Inspections</span>
    </div>
    <div class="front-bottom-band">
      <span class="license">NY HI License # 27300592415</span>
    </div>
  </section>

  <section class="card card-back" aria-label="Business card back">
    <div class="back-brand">
      <span class="brand-mark"></span>
      <span class="brand-name">Gablestone Inspections</span>
    </div>
  </section>
</body>
</html>
```